Larkmoor Blind Company / Blind Sale postcard mailer

I need a Design for a two sided postcard, advertising products for our company. One side will mainly show blinds & shutters, and the "call out" will be "Blind Sale / $59.99 per window". Then a place underneath for details. The other side of the card can showcase our other products (shades, exterior, etc). I would like the overall look and feel of the card to resemble the website design and colors, etc, you see at www.quillstonehome.example and www.fernwickdecor.example. You can use any images from my Stashbin page here: https://www.stashbin.example/sh/4kdmq8rtzvewplx/QQT2HHjbWpaLm731gxJtRsZ?dl=0

Use images from the Birchwave folder in Stashbin.
Also, my website for reference is www.larkmoorblinds.example
Larkmoor Blind Company

The printed card will be very plastic, heavy glossy. Heavier than most. I want the card to be as striking as possible, harder for customer to throw away. Trying to avoid lots of clutter on the card. Custom Template attached.

Target Market(s)

Card will be targeted mainly to new homeowners, especially new construction homes

Industry/Entity Type

It Company

Font styles to use
Serif
Sans Serif

Requirements
Must have
• Clean, uncluttered look. Best looking images. Logo somewhere on card. Open to changing the color of logo (i.e., if whites and greys are the main color, could do a white and grey version of logo..)

```html
<!DOCTYPE html>
<html lang="en">
<head>
<meta charset="utf-8">
<title>Larkmoor Blind Company – Blind Sale Postcard</title>
<link rel="stylesheet" href="https://fonts.googleapis.com/css2?family=Oswald:wght@500;600&family=Open+Sans:ital,wght@0,400;0,700;1,400&display=swap">
<style>
  :root {
    --page: #e8e5e0;
    --navy: #1c2434;
    --navy-deep: #121824;
    --blue: #2f66c9;
    --blue-light: #5b95dc;
    --white: #ffffff;
    --ink: #2a2f38;
    --grey-text: #5d6470;
    --pale-text: #c6cfdd;
    --stamp: #d6d6d6;
    --photo-warm-a: #d9cfc1;
    --photo-warm-b: #9d8a72;
    --photo-cool-a: #cfd5dc;
    --photo-cool-b: #6f7c8c;
  }
  * { box-sizing: border-box; margin: 0; padding: 0; }
  html, body { width: 826px; height: 1200px; overflow: hidden; }
  body { background: var(--page); font-family: "Open Sans", sans-serif; position: relative; }

  .postcard {
    position: absolute; left: 73px; width: 680px; height: 410px;
    background: var(--white); overflow: hidden;
    box-shadow: 0 6px 18px rgba(0,0,0,.25);
  }
  .postcard--front { top: 140px; }
  .postcard--back { top: 640px; }
  .shapes { position: absolute; inset: 0; }
  .abs { position: absolute; }

  .photo { position: absolute; }
  .photo--room { left: 0; top: 0; width: 400px; height: 250px;
    background: linear-gradient(135deg, var(--photo-warm-a), var(--photo-warm-b)); }
  .photo--detail { left: 24px; top: 276px; width: 146px; height: 68px;
    background: linear-gradient(135deg, var(--photo-warm-a), var(--photo-warm-b)); }
  .photo--shade { left: 22px; top: 96px; width: 134px; height: 70px;
    background: linear-gradient(135deg, var(--photo-warm-a), var(--photo-warm-b)); }
  .photo--office { left: 168px; top: 96px; width: 140px; height: 70px;
    background: linear-gradient(135deg, var(--photo-cool-a), var(--photo-cool-b)); }

  .sale { left: 414px; top: 26px; font-family: "Oswald", sans-serif; text-transform: uppercase; line-height: 1; white-space: nowrap; }
  .sale__price { color: var(--blue-light); font-size: 22px; font-weight: 500; }
  .sale__unit { color: var(--white); font-size: 38px; font-weight: 600; margin-top: 6px; }

  .brand { left: 614px; top: 22px; width: 54px; height: 42px; background: var(--blue);
    display: flex; align-items: center; justify-content: center; text-align: center;
    color: var(--white); font-size: 6.5px; font-weight: 700; line-height: 1.3; text-transform: uppercase; }

  .intro { left: 418px; top: 132px; width: 248px; color: var(--pale-text);
    font-size: 8.5px; line-height: 1.45; }

  .reasons { left: 192px; top: 274px; width: 470px; }
  .reasons__title { font-family: "Oswald", sans-serif; font-weight: 500; color: var(--blue);
    font-size: 17px; text-transform: uppercase; letter-spacing: .2px; }
  .reasons__text { margin-top: 5px; font-style: italic; color: var(--grey-text); font-size: 9.5px; line-height: 1.4; }

  .about { left: 22px; top: 16px; width: 286px; color: var(--pale-text); font-size: 8.5px; line-height: 1.45; }
  .contact { left: 22px; top: 193px; font-family: "Oswald", sans-serif; font-weight: 600;
    color: var(--white); font-size: 22px; text-transform: uppercase; white-space: nowrap; }
  .tagline { left: 22px; top: 262px; font-weight: 700; color: var(--blue); font-size: 12.5px; text-transform: uppercase; }
  .website { left: 22px; top: 284px; font-weight: 700; color: var(--ink); font-size: 16px; letter-spacing: .3px; }
  .stamp { left: 596px; top: 20px; width: 56px; height: 62px; background: var(--stamp); }
</style>
</head>
<body>

<section class="postcard postcard--front" aria-label="Postcard front">
  <div class="photo photo--room" role="img" aria-label="Bright living room with wood blinds on tall windows"></div>
  <svg class="shapes" width="680" height="410" viewBox="0 0 680 410" aria-hidden="true">
    <polygon points="398,0 680,0 680,250 360,250" fill="var(--navy)"/>
    <polygon points="380,0 398,0 360,250 342,250" fill="var(--blue)"/>
    <rect x="0" y="250" width="680" height="12" fill="var(--blue)"/>
    <rect x="18" y="270" width="158" height="80" fill="none" stroke="var(--blue)" stroke-width="3"/>
    <rect x="0" y="364" width="680" height="46" fill="var(--navy-deep)"/>
    <polygon points="0,364 300,364 285,376 0,376" fill="var(--blue)"/>
    <polygon points="420,398 680,398 680,410 408,410" fill="var(--blue)"/>
  </svg>
  <div class="photo photo--detail" role="img" aria-label="Close view of wood blinds in a window"></div>

  <div class="abs sale">
    <div class="sale__price">Blind Sale / $59.99</div>
    <div class="sale__unit">Per Window</div>
  </div>
  <div class="abs brand">Larkmoor<br>Blind<br>Company</div>
  <p class="abs intro">Wood blinds are a versatile custom window treatment that can work beautifully in any window. Manufactured from a variety of North American hardwoods, the finish is crafted to last for years and gives lasting warmth to every room.</p>

  <div class="abs reasons">
    <h2 class="reasons__title">Shutters are a great decorating choice for many reasons</h2>
    <p class="reasons__text">From a design viewpoint, they easily blend with the architectural elements of most windows, and can compliment both traditional and contemporary styles. They will elegantly combine many desired features, such as light control, privacy, energy efficiency, and noise reduction. Shutters enhance window beauty from both inside and outside.</p>
  </div>
</section>

<section class="postcard postcard--back" aria-label="Postcard back">
  <svg class="shapes" width="680" height="410" viewBox="0 0 680 410" aria-hidden="true">
    <rect x="0" y="0" width="330" height="180" fill="var(--navy)"/>
    <polygon points="0,180 360,180 330,236 0,236" fill="var(--blue)"/>
    <polygon points="330,0 344,0 344,180 330,180" fill="var(--blue)"/>
    <rect x="0" y="364" width="680" height="46" fill="var(--navy-deep)"/>
    <polygon points="0,364 300,364 285,376 0,376" fill="var(--blue)"/>
    <polygon points="420,398 680,398 680,410 408,410" fill="var(--blue)"/>
  </svg>
  <p class="abs about">Cellular shades are a classic, elegant and functional solution for your windows. Available in a variety of blackout and translucent fabrics which are made with crisp pleats, the shade keeps its shape and helps insulate rooms, lowering your energy bill year round.</p>
  <div class="photo photo--shade" role="img" aria-label="Cellular shade lowered over a window"></div>
  <div class="photo photo--office" role="img" aria-label="Home office with shades on the windows"></div>
  <div class="abs contact">Contact us at – 404-555-0186</div>
  <div class="abs tagline">The finest window treatment products available</div>
  <div class="abs website">www.larkmoorblinds.example</div>
  <div class="abs stamp"></div>
</section>

</body>
</html>
```